Bramwell Joinery Website

My client Bramwell Joinery is looking for a redesign for a Word Press Website. Their current site is at www.bramwelljoinery.example They are a custom cabinet company, but also create bathroom, living room, bar and entertainment and bedroom cabinets too. They would like a design that emulates the master craftsman work they do yet a contemporary style.

Their current site was designed using Flash elements.

Target Market(s)

Home owners and builders of high end homes

Industry/Entity Type

Entertainment

Font styles to use
Serif
Decorative

Requirements
Must have
• Must show their work and logo using a contemporary style.
Nice to have
• Sliders that showcase their projects.

```html
<!DOCTYPE html>
<html lang="en">
<head>
<meta charset="utf-8">
<title>Bramwell Joinery</title>
<link href="https://fonts.googleapis.com/css2?family=Open+Sans:wght@400;600;700&family=Arimo:wght@400&family=Tinos:wght@700&display=swap" rel="stylesheet">
<style>
:root{
  --green:#3aa532;
  --green-dark:#1f7a1c;
  --green-light:#5cc24f;
  --text:#333;
  --muted:#555;
  --red:#c0392b;
  --grey-band:#ebebeb;
  --footer:#222;
  --footer-bottom:#1a1a1a;
  --footer-text:#ddd;
  --footer-muted:#888;
  --white:#fff;
}
*{box-sizing:border-box;margin:0;padding:0}
html,body{width:1200px;height:2387px;overflow:hidden}
body{position:relative;background:var(--white);font-family:"Open Sans",sans-serif;color:var(--text)}
.abs{position:absolute}

/* header */
.site-header{position:absolute;left:0;top:0;width:1200px;height:166px}
.call{left:99px;top:70px;font-size:14px;font-weight:700;color:#444;display:flex;align-items:center;gap:12px}
.brand{left:440px;top:60px;width:320px;display:flex;align-items:center;justify-content:center;gap:12px}
.brand-dot{width:22px;height:22px;border-radius:50%;background:var(--green)}
.brand-name{font-size:28px;font-weight:700;color:var(--green-dark)}
.search{left:923px;top:68px;width:178px;height:29px;display:flex}
.search-field{flex:1;border:1px solid #ddd;font-size:10px;color:#aaa;padding:8px 9px;line-height:12px}
.search-btn{width:38px;background:#888;display:flex;align-items:center;justify-content:center}

/* nav */
.main-nav{left:0;top:166px;width:1200px;height:43px;background:linear-gradient(#5cc24f,#2e9a28);display:flex;padding-left:99px}
.main-nav a{font-family:"Arimo",sans-serif;font-size:13px;color:var(--white);text-decoration:none;line-height:43px;padding:0 13px;border-right:1px solid rgba(255,255,255,.15)}
.main-nav a.active{background:var(--green-dark);padding:0 25px}

/* hero */
.hero{left:0;top:209px;width:1200px;height:498px;
  background:
    radial-gradient(ellipse 180px 150px at 345px 200px,rgba(150,165,150,.85),transparent 70%),
    radial-gradient(ellipse 220px 170px at 1040px 210px,rgba(170,185,170,.85),transparent 70%),
    radial-gradient(ellipse 520px 110px at 800px 420px,rgba(140,70,35,.9),transparent 70%),
    linear-gradient(180deg,#6d625a 0%,#9a8d80 30%,#7a6a5c 55%,#d8d3cc 78%,#bdb6ad 100%)}
.hero-caption{left:161px;top:179px;width:877px;height:137px;border:1px solid rgba(255,255,255,.8);background:rgba(0,0,0,.28);text-align:center;color:var(--white)}
.hero-title{font-family:"Tinos",serif;font-size:35px;font-weight:700;margin-top:18px;letter-spacing:.5px}
.hero-text{font-size:11px;line-height:17px;margin:10px auto 0;width:815px}
.dots{left:0;right:0;top:112px;display:flex;justify-content:center;gap:6px}
.dots span{width:10px;height:10px;border-radius:50%;border:1px solid #ddd}
.dots span.on{background:var(--green);border-color:var(--green)}

/* sections */
.section-title{position:absolute;left:0;width:1200px;text-align:center;font-size:23px;font-weight:700;color:#3b3b3b}
.card{position:absolute;top:804px;width:309px;height:382px;background:var(--white);box-shadow:0 1px 5px rgba(0,0,0,.25);text-align:center}
.card::after{content:"";position:absolute;left:20px;right:20px;bottom:-12px;height:12px;background:radial-gradient(ellipse at top,rgba(0,0,0,.28),transparent 70%)}
.card-photo{margin:6px;height:224px}
.card-title{font-size:15px;font-weight:700;margin-top:23px;color:#333}
.card-text{font-size:11px;line-height:20px;color:var(--muted);margin:8px 14px 0}
.view-more{font-size:11px;color:var(--red);margin-top:10px}

.video-band{left:0;top:1230px;width:1200px;height:530px;background:var(--grey-band)}
.video{left:390px;top:85px;width:425px;height:288px;
  background:
    radial-gradient(ellipse 120px 130px at 290px 110px,rgba(225,218,205,.95),transparent 70%),
    radial-gradient(ellipse 220px 60px at 180px 260px,rgba(215,205,190,.9),transparent 70%),
    linear-gradient(160deg,#2e261f,#5a4c3f 40%,#9b8f80 65%,#4d4238)}
.play{left:190px;top:122px}
.video-text{left:140px;top:398px;width:920px;text-align:center;font-size:11.5px;line-height:20px;color:#444}
.video-text .link{color:var(--red)}
.btn-green{left:523px;top:463px;width:122px;height:37px;background:linear-gradient(#4cbf40,#2a9324);color:var(--white);font-family:"Arimo",sans-serif;font-size:13px;text-align:center;line-height:37px}

.thumb{position:absolute;top:1854px;width:236px;height:164px;border:4px solid var(--white);box-shadow:0 1px 4px rgba(0,0,0,.3)}

/* footer */
.site-footer{left:0;top:2056px;width:1200px;height:247px;background:var(--footer);color:var(--footer-text)}
.f-col{position:absolute;top:52px}
.f-head{font-size:13.5px;font-weight:700;color:var(--white)}
.f-head.green{color:var(--green-light)}
.f-col p{font-size:11px;line-height:20px;margin-top:30px}
.f-col ul{list-style:none;margin-top:30px}
.f-col li{font-size:11px;line-height:20px;padding-left:17px;position:relative}
.f-col li::before{content:"›";position:absolute;left:0;color:var(--footer-muted)}
.newsletter{display:flex;margin-top:24px}
.newsletter .field{width:178px;height:33px;background:#1a1a1a;font-size:10px;color:#666;padding:10px}
.newsletter .go{width:66px;height:33px;background:var(--green);color:var(--white);font-size:11px;text-align:center;line-height:33px}

.footer-bottom{left:0;top:2303px;width:1200px;height:84px;background:var(--footer-bottom);color:var(--footer-muted);font-size:11px}
.footer-bottom .links{left:99px;top:25px}
.footer-bottom .copy{left:99px;top:50px}
.social{left:1006px;top:28px;display:flex;gap:8px}
.social span{width:26px;height:26px;border-radius:50%;border:1px solid #777;display:flex;align-items:center;justify-content:center}
</style>
</head>
<body>

<header class="site-header">
  <div class="abs call">
    <svg width="10" height="16" viewBox="0 0 10 16"><rect x="0.75" y="0.75" width="8.5" height="14.5" rx="1.5" fill="none" stroke="#555" stroke-width="1.5"/><circle cx="5" cy="12.5" r="1" fill="#555"/></svg>
    CALL US : (08) 555 010 20
  </div>
  <div class="abs brand"><span class="brand-dot"></span><span class="brand-name">Bramwell Joinery</span></div>
  <div class="abs search">
    <div class="search-field">SEARCH</div>
    <div class="search-btn"><svg width="14" height="14" viewBox="0 0 14 14"><circle cx="6" cy="6" r="4.3" fill="none" stroke="#fff" stroke-width="1.8"/><line x1="9.2" y1="9.2" x2="13" y2="13" stroke="#fff" stroke-width="2"/></svg></div>
  </div>
</header>

<nav class="abs main-nav">
  <a class="active">HOME</a><a>WHO WE ARE</a><a>GETTING STARTED</a><a>CONTACT US</a><a>CUSTOMER EXPERIENCE</a><a>PROFESSIONAL</a><a>PORTFOLIO</a><a>CABINET HARDWARE</a>
</nav>

<section class="abs hero" role="img" aria-label="Modern kitchen with timber-topped island, pendant lights and large windows">
  <div class="abs hero-caption">
    <h1 class="hero-title">PRAESENTIUM VOLUPTATUM DELENITI ATQUE</h1>
    <p class="hero-text">"Lorem ipsum dolor sit amet, consectetur adipiscing elit, sed do eiusmod tempor incididunt ut labore et dolore magna aliqua. Ut enim ad minim veniam, quis nostrud exercitation ullamco laboris nisi ut aliquip"</p>
    <div class="abs dots"><span></span><span></span><span class="on"></span></div>
  </div>
</section>

<h2 class="section-title" style="top:742px">OUR WORK</h2>
<article class="card" style="left:99px">
  <div class="card-photo" role="img" aria-label="White kitchen cabinetry with built-in oven and dark wood floor" style="background:radial-gradient(ellipse 150px 80px at 190px 120px,rgba(235,230,222,.95),transparent 70%),linear-gradient(180deg,#6b4a32 0%,#b9aa98 25%,#e2ddd5 55%,#4a2e1c 85%,#2e1b10 100%)"></div>
  <h3 class="card-title">ACCUSANTIUM DOLOREMQUE</h3>
  <p class="card-text">Must explain to you how all this mistaken idea of denouncing pleasure and praising pain was born and expound the actual teachings</p>
  <p class="view-more">VIEW MORE &nbsp;»</p>
</article>
<article class="card" style="left:444px">
  <div class="card-photo" role="img" aria-label="Black painted kitchen island with panelled doors" style="background:radial-gradient(ellipse 110px 90px at 150px 130px,#18130f,transparent 75%),linear-gradient(180deg,#d8d0bf 0%,#a8987e 25%,#2a221c 50%,#1c1612 75%,#6a4a30 100%)"></div>
  <h3 class="card-title">ACCUSANTIUM DOLOREMQUE</h3>
  <p class="card-text">Must explain to you how all this mistaken idea of denouncing pleasure and praising pain was born and expound the actual teachings</p>
  <p class="view-more">VIEW MORE &nbsp;»</p>
</article>
<article class="card" style="left:791px">
  <div class="card-photo" role="img" aria-label="Long white galley kitchen with range hood and dark floor" style="background:radial-gradient(ellipse 90px 70px at 200px 70px,rgba(240,236,230,.95),transparent 70%),linear-gradient(180deg,#7a6a5a 0%,#c9c2b8 35%,#e6e2dc 55%,#3a2a1e 80%,#22170f 100%)"></div>
  <h3 class="card-title">ACCUSANTIUM DOLOREMQUE</h3>
  <p class="card-text">Must explain to you how all this mistaken idea of denouncing pleasure and praising pain was born and expound the actual teachings</p>
  <p class="view-more">VIEW MORE &nbsp;»</p>
</article>

<section class="abs video-band">
  <h2 class="section-title" style="top:28px">WATCH OUR VIDEO</h2>
  <div class="abs video" role="img" aria-label="Video still of a cream kitchen with pendant lights and stone hood">
    <svg class="abs play" width="46" height="46" viewBox="0 0 46 46"><circle cx="23" cy="23" r="21" fill="rgba(255,255,255,.25)" stroke="rgba(255,255,255,.7)" stroke-width="2"/><path d="M18 14 L32 23 L18 32 Z" fill="rgba(255,255,255,.8)"/></svg>
  </div>
  <p class="abs video-text">At Bramwell Joinery, we've been designing and manufacturing the Midwest's finest custom cabinets and fixtures since 1966. From single cabinets to room remodels to entire home installations, our expert artisans help turn the house you live in to the home you've always dreamed of. - See more at:<br><span class="link">http://www.bramwelljoinery.example/#sthash.QCmEjMnM.dpuf</span></p>
  <div class="abs btn-green">CLICK TO VIEW</div>
</section>

<h2 class="section-title" style="top:1794px">PHOTO GALLERY</h2>
<div class="thumb" style="left:99px;background:radial-gradient(ellipse 90px 40px at 110px 120px,rgba(230,225,215,.9),transparent 70%),linear-gradient(180deg,#7a6a52 0%,#cfc6b4 40%,#a8957a 70%,#6e5c46 100%)" role="img" aria-label="Cream kitchen with granite island"></div>
<div class="thumb" style="left:353px;background:radial-gradient(ellipse 60px 50px at 110px 80px,rgba(200,160,110,.85),transparent 70%),linear-gradient(180deg,#5a6a64 0%,#a9b6b0 40%,#8a9c96 70%,#4e5c57 100%)" role="img" aria-label="Blue-grey vanity cabinets with lamp"></div>
<div class="thumb" style="left:610px;background:radial-gradient(ellipse 110px 40px at 120px 40px,rgba(240,210,120,.9),transparent 70%),radial-gradient(ellipse 100px 40px at 120px 120px,rgba(90,60,30,.9),transparent 70%),linear-gradient(180deg,#2a1d12 0%,#8a6a34 40%,#3a2616 100%)" role="img" aria-label="Dark wood kitchen with curved island and pendant lights"></div>
<div class="thumb" style="left:864px;background:radial-gradient(ellipse 50px 40px at 130px 50px,rgba(210,200,190,.85),transparent 70%),linear-gradient(180deg,#4a2616 0%,#a8683e 40%,#7a4222 70%,#3b2014 100%)" role="img" aria-label="Cherry wood kitchen with range hood"></div>

<footer class="abs site-footer">
  <div class="f-col" style="left:99px;width:275px">
    <h4 class="f-head green">ABOUT BRAMWELL</h4>
    <p>Lorem ipsum dolor sit amet, consectetur adipisicing elit, sed do eiusmod tempor incididunt ut labore et dolore magna aliqua. Ut enim ad minim veniam, quis nostrud exercitation ullamco laboris nisi ut aliquip ex ea commodo</p>
  </div>
  <div class="f-col" style="left:471px">
    <h4 class="f-head">LINKS</h4>
    <ul><li>Register</li><li>Log in</li><li>Entries RSS</li><li>Comments RSS</li><li>Pressroom.org</li></ul>
  </div>
  <div class="f-col" style="left:665px">
    <h4 class="f-head">MORE INFO</h4>
    <ul><li>Help Center</li><li>Terms of Use</li><li>About Studio</li><li>Studio Blog</li><li>Careers</li></ul>
  </div>
  <div class="f-col" style="left:853px;width:243px">
    <h4 class="f-head">NEWSLETTER</h4>
    <p style="text-align:justify;width:229px">Excepteur sint occaecat cupidatat non proident, sunt in culpa qui officia deserunt mollit anim id est laborum.</p>
    <div class="newsletter"><div class="field">EMAIL ADDRESS</div><div class="go">SIGN UP</div></div>
  </div>
</footer>

<div class="abs footer-bottom">
  <div class="abs links">Home | Who We Are | Getting Started | Contact Us | Customer Experience | Professional | Portfolio | Cabinet Hardware</div>
  <div class="abs copy">© 2015 Bramwell Joinery.Allrights Reserved.</div>
  <div class="abs social">
    <span><svg width="12" height="12" viewBox="0 0 12 12"><circle cx="9" cy="2.5" r="1.6" fill="#888"/><circle cx="3" cy="6" r="1.6" fill="#888"/><circle cx="9" cy="9.5" r="1.6" fill="#888"/><path d="M3 6 L9 2.5 M3 6 L9 9.5" stroke="#888" stroke-width="1"/></svg></span>
    <span><svg width="12" height="12" viewBox="0 0 12 12"><circle cx="2.5" cy="9.5" r="1.4" fill="#888"/><path d="M1.5 5.5 A5 5 0 0 1 6.5 10.5" fill="none" stroke="#888" stroke-width="1.4"/><path d="M1.5 1.8 A8.7 8.7 0 0 1 10.2 10.5" fill="none" stroke="#888" stroke-width="1.4"/></svg></span>
    <span><svg width="12" height="12" viewBox="0 0 12 12"><path d="M4 2.5 L10 6 L4 9.5 Z" fill="#888"/></svg></span>
  </div>
</div>

</body>
</html>
```